Business Card Design for Tax Accounting Company

I need design files that can be edited to add new professional designations onto the end of my name once complete. I need design files that can be edited for new employees. I also need the design files to be able to upload into CardNest for new orders. I've attached multiple logo files with varying file extensions to help with the design.
Please include the following contact information:
Marcus Tellan, CFP®, EA, CTC, CEPA
Founder & CEO
C (480) 517.3082
F (623) 389.5170
718 W Larkspur Ave
Mesa, AZ 85210
Updates
I need the business card to include the following contact info:
C: (480)517.3082
F: (623) 389.5170
mt@RidgewayLedgerGroup.com
www.MarcusRTellan.com
Address to be included is
718 W Larkspur Ave
Mesa, AZ 85210
Business Cards are double sided
Target Market(s)
Business owners $1M+ annual revenue, especially for the construction and technology industries
Industry/Entity Type
Accounting & Tax
Contact Information for Business Card
Contact information and logo
Look and feel
Each slider illustrates characteristics of the customer's brand and the style your logo design should communicate.

```html
<!DOCTYPE html>
<html lang="en">
<head>
<meta charset="utf-8">
<title>Ridgeway Ledger Group – Business Card</title>
<link href="https://fonts.googleapis.com/css2?family=Poppins:wght@300;400;600;700&display=swap" rel="stylesheet">
<style>
  :root {
    --stage: #d0d0d0;
    --navy: #012766;
    --gold: #ffd500;
    --white: #ffffff;
    --rule: rgba(255,255,255,0.55);
    --shadow: 4px 6px 10px rgba(0,0,0,0.22);
  }
  * { box-sizing: border-box; margin: 0; padding: 0; }
  html, body { width: 720px; height: 1200px; overflow: hidden; background: var(--stage); }
  body { font-family: "Poppins", sans-serif; position: relative; }

  .card {
    position: absolute; left: 60px; width: 600px; height: 342px;
    box-shadow: var(--shadow); overflow: hidden;
  }
  .card--front { top: 200px; background: var(--navy); color: var(--white); }
  .card--back  { top: 602px; background: var(--white); }

  .brand-mark {
    position: absolute; display: flex; align-items: center; gap: 10px;
    font-weight: 600; white-space: nowrap;
  }
  .card--front .brand-mark { right: 37px; top: 74px; color: var(--white); font-size: 17px; }
  .brand-dot { width: 34px; height: 34px; border-radius: 50%; background: var(--gold); flex: none; }

  .person { position: absolute; left: 37px; top: 134px; }
  .person__name { font-size: 24px; font-weight: 700; line-height: 1.1; letter-spacing: -0.2px; }
  .person__name .surname { color: var(--gold); }
  .person__creds { font-size: 13px; font-weight: 600; margin-top: 2px; }
  .person__creds sup { font-size: 7px; }

  .divider { position: absolute; left: 37px; right: 37px; top: 209px; height: 1px; background: var(--rule); }

  .contact {
    position: absolute; display: flex; align-items: center;
    font-size: 15px; font-weight: 300; line-height: 16px; white-space: nowrap;
    letter-spacing: -0.1px;
  }
  .contact svg { width: 14px; height: 14px; fill: var(--gold); flex: none; }
  .contact--left svg { margin-right: 23px; }
  .contact--right svg { margin-right: 22px; }
  .contact--left  { left: 37px; }
  .contact--right { left: 283px; }
  .row-1 { top: 235px; }
  .row-2 { top: 260px; }
  .row-3 { top: 292px; }

  .card--back .brand-mark {
    left: 50%; top: 50%; transform: translate(-50%, -50%);
    color: var(--navy); font-size: 28px; gap: 14px;
  }
  .card--back .brand-dot { width: 46px; height: 46px; }
</style>
</head>
<body>

<section class="card card--front">
  <div class="brand-mark"><span class="brand-dot"></span>Ridgeway Ledger Group</div>

  <div class="person">
    <div class="person__name">Marcus <span class="surname">Tellan</span></div>
    <div class="person__creds">CFP<sup>®</sup>, EA, CTC, CEPA</div>
  </div>

  <div class="divider"></div>

  <div class="contact contact--left row-1">
    <svg viewBox="0 0 16 16" aria-hidden="true"><path d="M3.6 1l2.3 2.9-1.3 1.6c.9 2 2.6 3.8 4.8 4.9l1.6-1.3L14 11.4l-1.2 2.8C7 14.4 1.6 9 1.6 2.4z"/></svg>
    <span>480 517 3082</span>
  </div>
  <div class="contact contact--left row-2">
    <svg viewBox="0 0 16 16" aria-hidden="true"><path d="M8 1a7 7 0 100 14A7 7 0 008 1zm-1 12.4A5.5 5.5 0 013 5.3l2 1.3v1.5l2 1.4zm5.6-2.5L11 9.8V8L8.6 6.5V4.8l1.8-1.5a5.5 5.5 0 012.2 7.6z"/></svg>
    <span>www.MarcusRTellan.com</span>
  </div>
  <div class="contact contact--left row-3">
    <svg viewBox="0 0 16 16" aria-hidden="true"><path d="M8 1a4.8 4.8 0 00-4.8 4.8C3.2 9.5 8 15 8 15s4.8-5.5 4.8-9.2A4.8 4.8 0 008 1zm0 6.8a2 2 0 110-4 2 2 0 010 4z"/></svg>
    <span>718 W Larkspur Ave Mesa, AZ, 85210</span>
  </div>

  <div class="contact contact--right row-1">
    <svg viewBox="0 0 16 16" aria-hidden="true"><path d="M1 5h3v10H1zM5 4h10v11H5zm1-3h6v2H6zM7 6v2h6V6zm0 4v1.5h1.5V10zm2.5 0v1.5H11V10zM12 10v1.5h1.5V10zm-5 2.5V14h1.5v-1.5zm2.5 0V14H11v-1.5zm2.5 0V14h1.5v-1.5z"/></svg>
    <span>623 389 5170</span>
  </div>
  <div class="contact contact--right row-2">
    <svg viewBox="0 0 16 16" aria-hidden="true"><path d="M1 3h14v1.6L8 9 1 4.6zm0 3.4l7 4.4 7-4.4V13H1z"/></svg>
    <span>mt@RidgewayLedgerGroup.com</span>
  </div>
</section>

<section class="card card--back">
  <div class="brand-mark"><span class="brand-dot"></span>Ridgeway Ledger Group</div>
</section>

</body>
</html>
```